HVAC contracting company needs a mordern business card!

We need a business card design for our Air condition company based in UAE since 1988. We specialize in the installation, maintenance of Air-condition equipments for both residential & commercial projects. We would like to have a card design that is modern.The card design should be relevant to our work.

Target Market(s)

MNCs, local house owners

Industry/Entity Type

Hvac

Contact Information for Business Card

Tel : +971 9 5558142, +971 9 5558196
Fax : +971 9 5558103
Mobile : +971 50 5553614
PO. Box : 382, Fujairah, U.A.E
Email : info@kdrbreeze.example
Website : www.kdrbreezeco.example

Requirements
Must have
• - Include all contact details & company logos
• - include the logos of the brands that we support
Nice to have
• Since most of our clients are arabic speak/arab origins, arabic translation of the business card would great to have!
Should not have
• Dark colors/background

```html
<!DOCTYPE html>
<html lang="en">
<head>
<meta charset="utf-8">
<title>Kadir Breeze Co. — Business Card</title>
<link href="https://fonts.googleapis.com/css2?family=Arimo:wght@400;700&family=Noto+Naskh+Arabic:wght@400;700&display=swap" rel="stylesheet">
<style>
  :root {
    --page: #ecebe8;
    --card: #ffffff;
    --ink: #1b1b1f;
    --brand-red: #e3141b;
    --lavender: #e6e4f7;
    --band-a: #6f6fd6;
    --band-b: #c9c8f1;
    --muted: #4b4b55;
  }
  * { margin: 0; padding: 0; box-sizing: border-box; }
  html, body { width: 1200px; height: 1013px; overflow: hidden; background: var(--page); }
  body { position: relative; font-family: "Arimo", Arial, sans-serif; color: var(--ink); }

  .card {
    position: absolute; left: 276px; width: 683px; height: 352px;
    background: var(--card); border-radius: 22px; overflow: hidden;
    box-shadow: 0 6px 18px rgba(0,0,0,.18);
  }
  .card--front { top: 132px; }
  .card--back { top: 537px; }
  .card__decor { position: absolute; inset: 0; }

  .ar { font-family: "Noto Naskh Arabic", "Times New Roman", serif; direction: rtl; }

  .mark-ring {
    position: absolute; border: 6px solid var(--brand-red); border-radius: 50%;
    display: flex; align-items: center; justify-content: center;
    color: var(--brand-red); font-weight: 700; text-align: center; line-height: 1.1;
  }

  .name-ar { position: absolute; font-weight: 700; white-space: nowrap; color: var(--ink); }
  .name-en { position: absolute; white-space: nowrap; color: var(--ink); letter-spacing: .3px; }

  /* front */
  .card--front .mark-ring { left: 157px; top: 45px; width: 96px; height: 96px; font-size: 12px; }
  .card--front .name-ar { left: 272px; top: 50px; width: 262px; font-size: 30px; text-align: right; }
  .card--front .name-en { left: 277px; top: 101px; font-size: 19px; }

  .services { position: absolute; left: 26px; top: 173px; font-size: 12.5px; line-height: 17.5px; list-style: none; }
  .services-divider { position: absolute; left: 340px; top: 164px; width: 1px; height: 82px; background: var(--ink); }
  .services-ar { position: absolute; right: 19px; top: 156px; font-size: 13.5px; line-height: 17px; text-align: right; list-style: none; }

  .band { position: absolute; left: 0; right: 0; top: 270px; height: 11px;
    background: linear-gradient(90deg, var(--band-b), var(--band-a) 50%, var(--band-b)); }
  .footer { position: absolute; left: 0; right: 0; top: 293px; bottom: 0;
    background: linear-gradient(90deg, #f4f3fb, var(--lavender) 40%, #f4f3fb 70%, var(--lavender)); }

  .phones { position: absolute; left: 28px; top: 298px; font-size: 9px; line-height: 11px; border-collapse: collapse; }
  .phones td { padding: 0 4px 3px 0; vertical-align: top; white-space: nowrap; }
  .phones .sep { border-left: 1px solid var(--ink); padding-left: 5px; }
  .phones .ar { font-size: 9px; line-height: 11px; text-align: right; }

  .postal { position: absolute; left: 384px; top: 302px; font-size: 9px; line-height: 16px; white-space: nowrap; }
  .postal .ar { font-size: 9px; line-height: 11px; }

  /* back */
  .card--back .mark-ring { left: 92px; top: 80px; width: 128px; height: 128px; font-size: 15px; }
  .card--back .name-ar { left: 250px; top: 90px; width: 350px; font-size: 40px; text-align: right; }
  .card--back .name-en { left: 251px; top: 156px; font-size: 28px; }

  .dealer-label { position: absolute; left: 289px; top: 283px; font-size: 14px; color: var(--muted); }
  .dealer-strip { position: absolute; left: 0; right: 0; top: 301px; bottom: 0;
    background: linear-gradient(90deg, #e3e2f6, #f7f7fc 50%, #e3e2f6);
    display: flex; align-items: center; justify-content: space-around; padding: 0 18px; }
  .dealer { font-size: 15px; font-weight: 700; color: var(--muted); display: flex; align-items: center; gap: 6px; }
  .dealer__dot { width: 16px; height: 16px; border-radius: 50%; background: #8d8cc9; }
</style>
</head>
<body>

<section class="card card--front" aria-label="Business card front">
  <svg class="card__decor" viewBox="0 0 683 352" aria-hidden="true">
    <defs>
      <linearGradient id="skyA" x1="0" y1="0" x2="1" y2="1">
        <stop offset="0" stop-color="#9fbaf2" stop-opacity=".85"/>
        <stop offset="1" stop-color="#ffffff" stop-opacity="0"/>
      </linearGradient>
      <linearGradient id="skyB" x1="1" y1="0" x2="0" y2="1">
        <stop offset="0" stop-color="#c7c5f0" stop-opacity=".8"/>
        <stop offset="1" stop-color="#ffffff" stop-opacity="0"/>
      </linearGradient>
    </defs>
    <polygon points="0,0 300,0 0,200" fill="url(#skyB)" opacity=".5"/>
    <polygon points="280,0 470,0 210,180" fill="url(#skyA)"/>
    <polygon points="683,40 683,270 470,270" fill="url(#skyB)"/>
    <polygon points="520,0 683,0 683,60" fill="url(#skyA)" opacity=".6"/>
  </svg>

  <div class="mark-ring">Kadir<br>Breeze</div>
  <div class="name-ar ar">شركة قدير بريز</div>
  <div class="name-en">KADIR BREEZE CO.</div>

  <ul class="services">
    <li>Maintenance &amp; Installation Of Lifts</li>
    <li>Maintenance &amp; Installation Of Central &amp; Split AC</li>
    <li>Installation Of False Ceiling &amp; Partitions</li>
    <li>Building Maintenance</li>
  </ul>
  <div class="services-divider"></div>
  <ul class="services-ar ar">
    <li>تركيب وصيانة المصاعد الكهربائية</li>
    <li>تركيب وصيانة التكييف المركزي</li>
    <li>اعمال وتركيب الفولس سيلنك</li>
    <li>تركيب قواطع وحواجز (بارتيشن)</li>
    <li>صيانة الادوات الالكترونية</li>
  </ul>

  <div class="band"></div>
  <div class="footer"></div>

  <table class="phones">
    <tr><td>Office</td><td>: +971 9 5558142 /<br>&nbsp;&nbsp;+971 9 5558196</td><td class="sep ar">٩٧١ ٩ ٥٥٥٨١٤٢ /<br>٩٧١ ٩ ٥٥٥٨١٩٦</td><td class="ar">: تليفون مكتب</td></tr>
    <tr><td>Fax</td><td>: +971 9 5558103</td><td class="sep ar">٩٧١ ٩ ٥٥٥٨١٠٣</td><td class="ar">: فاكس</td></tr>
    <tr><td>Mobile</td><td>: +971 50 5553614</td><td class="sep ar">٩٧١ ٥٠ ٥٥٥٣٦١٤</td><td class="ar">: متحرك</td></tr>
  </table>
  <div class="postal">
    <div>PO. Box : 382, Fujairah, U.A.E &nbsp;|&nbsp; <span class="ar">ص.ب ٣٨٢ الفجيرة ، ا.ع.م</span></div>
    <div>website : www.kdrbreezeco.example</div>
    <div>email : info@kdrbreeze.example</div>
  </div>
</section>

<section class="card card--back" aria-label="Business card back">
  <svg class="card__decor" viewBox="0 0 683 352" aria-hidden="true">
    <defs>
      <linearGradient id="skyC" x1="0" y1="0" x2="1" y2="1">
        <stop offset="0" stop-color="#9fbaf2" stop-opacity=".85"/>
        <stop offset="1" stop-color="#ffffff" stop-opacity="0"/>
      </linearGradient>
      <linearGradient id="skyD" x1="1" y1="0" x2="0" y2="1">
        <stop offset="0" stop-color="#b9b7ee" stop-opacity=".85"/>
        <stop offset="1" stop-color="#ffffff" stop-opacity="0"/>
      </linearGradient>
    </defs>
    <polygon points="0,0 380,0 0,150" fill="url(#skyD)" opacity=".5"/>
    <polygon points="300,0 390,0 230,120" fill="url(#skyC)"/>
    <polygon points="683,150 683,300 470,300" fill="url(#skyD)"/>
    <polygon points="0,200 140,300 0,300" fill="url(#skyC)" opacity=".4"/>
  </svg>

  <div class="mark-ring">Kadir<br>Breeze</div>
  <div class="name-ar ar">شركة قدير بريز</div>
  <div class="name-en">KADIR BREEZE CO.</div>

  <div class="dealer-label">Authorized Dealer.</div>
  <div class="dealer-strip">
    <span class="dealer">Arctiva</span>
    <span class="dealer">Polarix</span>
    <span class="dealer">Coolmark</span>
    <span class="dealer">Nordair</span>
    <span class="dealer">Frostline</span>
    <span class="dealer"><span class="dealer__dot"></span>Veloair</span>
  </div>
</section>

</body>
</html>
```